Harbrook Techlink Solutions

We need a Logo and Website for our company based in London. We are a IT recruitment company . We provide quality resources to top IT company across UK.

Industry/Entity Type

It Company

Number of Pages Required

4 page

```html
<!DOCTYPE html>
<html lang="en">
<head>
<meta charset="utf-8">
<title>Harbrook Techlink Solutions</title>
<link href="https://fonts.googleapis.com/css2?family=Open+Sans:ital,wght@0,400;0,600;0,700;1,700&family=Ubuntu:wght@500;700&family=Roboto+Condensed:wght@400;500&display=swap" rel="stylesheet">
<style>
:root{
  --frame:#e6e6e6;
  --navy:#1b1956;
  --navy-deep:#141246;
  --blue:#1a80d2;
  --blue-light:#3ba3e6;
  --heading-blue:#2b8fd2;
  --orange:#f7941d;
  --text:#333;
  --muted:#555;
  --white:#fff;
  --avatar:#c9d3de;
}
*{margin:0;padding:0;box-sizing:border-box}
html,body{width:760px;height:1200px;overflow:hidden}
body{background:var(--frame);font-family:"Open Sans",sans-serif;color:var(--text);position:relative}
.abs{position:absolute}
.page{position:absolute;left:10px;top:10px;width:740px;height:1150px;background:var(--white)}

/* hero */
.hero-photo{left:0;top:0;width:740px;height:474px;
  background:radial-gradient(ellipse at 62% 62%,#6d7f9c 0%,#3d5a86 25%,#1f3f73 50%,#112a55 80%),#112a55}
.brand{left:38px;top:74px;font-family:"Open Sans",sans-serif;font-weight:600;font-size:15px;color:var(--white);display:flex;align-items:center;gap:7px}
.brand-dot{width:14px;height:14px;border-radius:50%;background:var(--blue-light)}
.social{display:flex;gap:3px}
.social span{width:15px;height:15px;border-radius:2px;background:var(--blue)}
.social span:nth-child(4){background:var(--orange)}
.help-photo{left:588px;top:6px;width:42px;height:42px;border-radius:50%;border:2px solid #bcd;background:linear-gradient(#d9e3ee,#9fb4cb)}
.questions{left:635px;top:13px;width:93px;height:34px;background:var(--blue-light);border-radius:4px;color:var(--white);text-align:center}
.questions b{display:block;font-family:"Roboto Condensed",sans-serif;font-weight:500;font-size:11px;padding-top:3px}
.questions i{display:block;font-style:normal;font-size:7.5px;font-weight:700;background:var(--navy);border-radius:4px;margin:1px 3px 0;padding:2px 0}
.nav{left:304px;top:63px;width:424px;height:20px;background:var(--blue);border-radius:3px;display:flex;justify-content:center;align-items:center;gap:8px;font-family:"Roboto Condensed",sans-serif;font-size:8.5px;font-weight:500;color:var(--white)}
.headline{left:0;top:226px;width:740px;text-align:center;font-family:"Ubuntu",sans-serif;font-weight:700;font-size:25px;color:var(--orange)}
.lead{left:60px;top:257px;width:620px;text-align:center;font-style:italic;font-weight:700;font-size:13px;line-height:17px;color:var(--white)}
.cta{left:189px;top:325px;width:362px;height:44px;background:var(--orange);border-radius:3px;color:var(--white);font-family:"Ubuntu",sans-serif;font-weight:700;font-size:14px;display:flex;align-items:center;justify-content:center}

/* features */
.features{left:0;top:474px;width:740px;height:190px;background:var(--navy)}
.features .glow{left:370px;top:0;width:185px;height:190px;background:linear-gradient(#2a8ed8,#1e3f8a 60%,var(--navy))}
.feature{top:-14px;width:185px;text-align:center;color:var(--white)}
.feature-icon{display:block;margin:0 auto;width:66px;height:66px}
.feature h3{font-family:"Roboto Condensed",sans-serif;font-weight:400;font-size:14.5px;line-height:16px;height:40px;margin-top:13px}
.feature p{font-size:9.3px;line-height:12.4px;margin-top:4px;padding:0 14px}

/* content */
.section-title{font-family:"Roboto Condensed",sans-serif;font-size:15px;color:var(--heading-blue)}
.date{left:19px;top:721px;width:50px;height:56px;color:var(--white);text-align:center;border-radius:2px;overflow:hidden}
.date .top{background:var(--blue-light);height:36px;font-family:"Ubuntu",sans-serif;font-weight:700;font-size:17px;line-height:17px;padding-top:3px}
.date .top small{display:block;font-size:10px;line-height:11px}
.date .yr{background:var(--navy);height:20px;font-size:11px;font-weight:700;line-height:20px}
.post-title{left:80px;top:722px;width:210px;font-size:10.5px;font-weight:600;line-height:13px;color:#222}
.post-text{left:80px;top:750px;width:210px;font-size:9.3px;line-height:12.6px;color:var(--muted)}
.btn-more{left:80px;top:797px;width:67px;height:18px;background:#ddd;border-radius:3px;font-size:9px;font-weight:600;color:#444;display:flex;align-items:center;justify-content:center}
.news-title{left:20px;top:877px;font-size:10px;font-weight:700;color:#222}
.news-text{left:20px;top:891px;width:270px;font-size:9.3px;line-height:12.6px;color:var(--muted)}

.fb{left:297px;top:721px;width:210px;height:178px;border:1px solid #ddd;background:#fff}
.fb-cover{left:0;top:0;width:208px;height:80px;background:linear-gradient(120deg,#0d2a4c,#1b5f94 55%,#0b2240)}
.fb-name{left:52px;top:20px;font-size:9px;font-weight:700;color:var(--white)}
.fb-avatar{left:10px;top:12px;width:34px;height:34px;background:var(--white)}
.fb-btn{top:60px;height:14px;background:#f5f6f7;border:1px solid #ccc;font-size:7px;font-weight:600;color:#4b4f56;padding:0 5px;line-height:12px}
.fb-friends{left:6px;top:86px;width:186px;height:42px;border:1px solid #e5e5e5;font-size:7px;color:#555;padding:4px 5px}
.faces{display:flex;gap:2px;margin-top:3px}
.faces span{width:17px;height:17px;background:linear-gradient(#8a8e95,#5e6067)}
.fb-post{left:6px;top:134px;width:186px;height:44px;border:1px solid #e5e5e5}
.tweets{left:513px;top:721px;width:209px;height:178px;border:1px solid #ddd;background:#fff}
.tweet{left:36px;width:168px;font-size:7.3px;line-height:9.2px;color:#222}
.tweet small{display:block;font-size:6.4px;color:#444}
.tweet-avatar{left:9px;width:18px;height:18px;border-radius:50%;background:var(--avatar)}

/* footer */
.footer{left:0;top:984px;width:740px;height:165px;background:var(--navy)}
.foot-head{font-size:8.5px;font-weight:700;color:var(--orange)}
.foot-list{font-size:8px;line-height:13.4px;color:#c9d2ea;font-weight:600;list-style:none}
.contact{left:422px;font-size:9px;font-weight:600;color:#c9d2ea;line-height:11px}
.copyright{left:0;top:1170px;width:760px;text-align:center;font-size:7px;color:#333}
</style>
</head>
<body>
<div class="page">
  <!-- hero -->
  <div class="abs hero-photo" role="img" aria-label="Photograph of a hand touching a glowing screen with floating technology icons"></div>
  <div class="abs brand"><span class="brand-dot"></span>Harbrook Techlink Solutions</div>
  <div class="abs social" style="left:484px;top:20px"><span></span><span></span><span></span><span></span></div>
  <div class="abs help-photo" role="img" aria-label="Photograph of a support agent with headset"></div>
  <div class="abs questions"><b>QUESTIONS?</b><i>CALL 555-014-2290</i></div>
  <nav class="abs nav"><span>HOME</span>|<span>ABOUT US</span>|<span>IT SERVICES</span>|<span>NEWS &amp; EVENTS</span>|<span>BLOG</span>|<span>CONTACT US</span>|<span>SUPPORT</span></nav>
  <h1 class="abs headline">THE LEADER IN IT RECRUITMENT</h1>
  <p class="abs lead">Lorem ipsum dolor sit amet, consectetuer adipiscing elit, sed diam nonummy nibh euismod tincidunt ut laoreet dolore magna aliquam erat volutpat. Ut wisi enim ad minim veniam, quis nostrud exerci ullamcorper suscipit lobortis nisl ut aliquip ex ea commodo consequat. Duis autem vel eum.</p>
  <div class="abs cta">GET STARTED NOW AND WE DO IT RIGHT FOR YOU</div>

  <!-- features -->
  <section class="abs features">
    <div class="abs glow"></div>
    <div class="abs feature" style="left:0">
      <svg class="feature-icon" viewBox="0 0 66 66"><circle cx="33" cy="33" r="31" fill="#1a6fc4" stroke="#fff" stroke-width="3"/><path d="M19 34l10 10 19-21" fill="none" stroke="#fff" stroke-width="7" stroke-linecap="round" stroke-linejoin="round"/></svg>
      <h3>PROACTIVE</h3>
      <p>Lorem ipsum dolor sit amet, consec tetuer adipiscing elit, sed diam nonummy nibh euismod tincidunt ut laoreet dolore magna.</p>
    </div>
    <div class="abs feature" style="left:185px">
      <svg class="feature-icon" viewBox="0 0 66 66"><circle cx="33" cy="33" r="31" fill="#1a6fc4" stroke="#fff" stroke-width="3"/><circle cx="33" cy="33" r="17" fill="none" stroke="#fff" stroke-width="4"/><path d="M33 23v11h8" fill="none" stroke="#fff" stroke-width="3.5" stroke-linecap="round"/></svg>
      <h3>ROUND THE CLOCK<br>SUPPORT</h3>
      <p>Lorem ipsum dolor sit amet, consec tetuer adipiscing elit, sed diam nonummy nibh euismod tincidunt ut laoreet dolore magna.</p>
    </div>
    <div class="abs feature" style="left:370px">
      <svg class="feature-icon" viewBox="0 0 66 66"><circle cx="33" cy="33" r="31" fill="#1a6fc4" stroke="#fff" stroke-width="3"/><path d="M17 22h32v18H30l-8 7v-7h-5z" fill="#fff"/></svg>
      <h3>LIVE HELP DESK<br>SUPPORT</h3>
      <p>Lorem ipsum dolor sit amet, consec tetuer adipiscing elit, sed diam nonummy nibh euismod tincidunt ut laoreet dolore magna.</p>
    </div>
    <div class="abs feature" style="left:555px">
      <svg class="feature-icon" viewBox="0 0 66 66"><circle cx="33" cy="33" r="31" fill="#1a6fc4" stroke="#fff" stroke-width="3"/><circle cx="27" cy="33" r="10" fill="none" stroke="#fff" stroke-width="4"/><circle cx="39" cy="33" r="10" fill="none" stroke="#fff" stroke-width="4"/></svg>
      <h3>TRUSTED BUSINESS<br>PARTNERS</h3>
      <p>Lorem ipsum dolor sit amet, consec tetuer adipiscing elit, sed diam nonummy nibh euismod tincidunt ut laoreet dolore magna.</p>
    </div>
  </section>

  <!-- blog & news -->
  <h2 class="abs section-title" style="left:20px;top:692px">LATEST BLOG POST</h2>
  <div class="abs date"><div class="top">11<small>JAN</small></div><div class="yr">2016</div></div>
  <p class="abs post-title">Lorem ipsum dolor sit amet, consectetuer adipiscing elit.</p>
  <p class="abs post-text">Lorem ipsum dolor sit amet, consectetuer adipis cing elit, sed diam nonummy nibh euismod tincidunt ut laoreet dolore magna aliquam.</p>
  <div class="abs btn-more">READ MORE</div>
  <h2 class="abs section-title" style="left:20px;top:838px">LATEST NEWS</h2>
  <p class="abs news-title">Lorem ipsum dolor sit amet.</p>
  <p class="abs news-text">Lorem ipsum dolor sit amet, consectetuer adipiscing elit, sed diam nonummy nibh euismod tincidunt ut laoreet dolore magna aliquam erat volutpat.</p>

  <!-- social -->
  <h2 class="abs section-title" style="left:299px;top:692px">FROM SOCIAL MEDIA</h2>
  <div class="abs fb">
    <div class="abs fb-cover" role="img" aria-label="Cover image of a digital world map"></div>
    <div class="abs fb-avatar"></div>
    <div class="abs fb-name">Harbrook Techlink</div>
    <div class="abs fb-btn" style="left:10px">Like Page</div>
    <div class="abs fb-btn" style="left:142px">Book Now</div>
    <div class="abs fb-friends">Be the first of your friends to like this
      <div class="faces"><span></span><span></span><span></span><span></span><span></span><span></span><span></span><span></span><span></span></div>
    </div>
    <div class="abs fb-post">
      <div class="abs" style="left:6px;top:6px;width:32px;height:30px;background:linear-gradient(#7a8a6a,#4a5a40)" role="img" aria-label="Post thumbnail photograph"></div>
      <div class="abs" style="left:46px;top:14px;font-size:7.5px;font-weight:600;color:#365899">Harbrook Techlink</div>
      <div class="abs" style="left:46px;top:24px;font-size:6.5px;color:#90949c">8 hrs</div>
    </div>
  </div>
  <div class="abs tweets">
    <div class="abs" style="left:10px;top:8px;font-size:9px;font-weight:600;color:#333">TWEETS</div>
    <div class="abs" style="left:72px;top:4px;width:128px;height:17px;border:1px solid #ccc;background:#f5f5f5;border-radius:3px;font-size:7.5px;color:#333;display:flex;align-items:center;justify-content:center">Follow @HarbrookTech</div>
    <div class="abs tweet-avatar" style="top:37px"></div>
    <p class="abs tweet" style="top:32px"><small>Sept 29, 2015</small>Lorem ipsum dolor sit amet, consectetuer adip iscing elit, sed diam nonummy nibh euismod</p>
    <div class="abs tweet-avatar" style="top:77px"></div>
    <p class="abs tweet" style="top:72px"><small>Sept 25, 2015</small>Lorem ipsum dolor sit amet, consectetuer adi piscing elit, sed diam nonummy nibh euismod tincidunt ut laoreet dolore magna aliquam erat volutpat. Ut wisi enim ad minim veniam, quis nostrud exerci tation ullamcorper suscipit lobo rtis nisl ut aliquip ex ea commodo consequat tincidunt ut laoreet dolore magna aliquam erat.</p>
    <div class="abs" style="left:0;top:158px;width:207px;height:19px;background:#eee;font-size:7.5px;color:#333;padding:5px 10px">Tweet to @HarbrookTech</div>
  </div>

  <!-- footer -->
  <footer class="abs footer">
    <div class="abs foot-head" style="left:65px;top:21px">NAVIGATION</div>
    <ul class="abs foot-list" style="left:65px;top:37px"><li>About Us</li><li>IT Services</li><li>News &amp; Events</li><li>Blog</li><li>Contact Us</li><li>Support</li></ul>
    <div class="abs foot-head" style="left:160px;top:21px">IT RECRUITMENT SERVICES</div>
    <ul class="abs foot-list" style="left:160px;top:37px"><li>Hosted Exchange</li><li>Healthcare IT</li><li>Hardware as a Service</li><li>Network Care</li><li>Backup &amp; Disaster Recovery</li><li>Spam Protection</li><li>VoIP</li><li>Hosted Cloud IT</li></ul>
    <ul class="abs foot-list" style="left:280px;top:37px"><li>Cloud Computing</li><li>Virtual CIO</li><li>Outsourcing your IT</li><li>Server Care</li><li>Web Filtering &amp; Firewall</li><li>Mobile Office</li><li>Vendor Management</li></ul>
    <div class="abs foot-head" style="left:410px;top:21px">CONTACT INFO</div>
    <svg class="abs" style="left:410px;top:41px" width="8" height="11" viewBox="0 0 8 11"><path d="M4 11S0 6 0 4a4 4 0 018 0c0 2-4 7-4 7z" fill="#c9d2ea"/><circle cx="4" cy="4" r="1.5" fill="#1b1956"/></svg>
    <p class="abs contact" style="left:424px;top:40px">4623 Lorem Ipsum<br>Ashford Vale, 95001</p>
    <svg class="abs" style="left:409px;top:73px" width="10" height="8" viewBox="0 0 10 8"><path d="M0 3c0-3 10-3 10 0v1H7V2H3v2H0zM2 4h6l1 4H1z" fill="#c9d2ea"/></svg>
    <p class="abs contact" style="left:424px;top:71px">555-010-4477</p>
    <svg class="abs" style="left:409px;top:93px" width="10" height="7" viewBox="0 0 10 7"><rect width="10" height="7" fill="#c9d2ea"/><path d="M0 0l5 4 5-4" fill="none" stroke="#1b1956"/></svg>
    <p class="abs contact" style="left:424px;top:92px">support@harbrooktechlink.example</p>
    <div class="abs social" style="left:424px;top:126px"><span></span><span></span><span></span><span></span></div>
  </footer>
</div>
<p class="abs copyright">COPYRIGHT 2016 HARBROOK TECHLINK SOLUTIONS. ALL RIGHTS RESERVED.</p>
</body>
</html>
```